FACIAL COSMETICS BUSINESS CARD

WE ARE A DENTAL PRACTICE BUT ARE OPENING UP A BRANCH FOR FACILA COSMETICS, LIKE BOTOX, FILLERS, PEELS, ETC. GWEN AND MARISOL WILL BE RUNNING THAT PART OF THE BUSINESS.
OUR CURRENT CARD IS ATTACHED AND OUR LOGO IT ATTACHED TOO. THE LOGO HAS ON IT OLMEN DENTAL, I WOULD LIKE IT TO SAY OLMEN COSMETICS, THE PHONE NUMBERS ON IT HAS TO BE REPLACED BY THE ONES I GAVE PREVIOUSLY AND THE WEB ADDRESS HAS TO BE DELETED, THE OTHER SIDE OF THE CARD HAS A MAP WHICH HAS TO BE DELETED, ADD TWO DATE-TIME LINES, I LIKE THE CARDS TO BE SIMPLE AND CLEAN, SIZE HAS TO BE NO LARGER THAN 5CMx8.5CM.
THE CARD HAS TO BE MATTE, I HATE GLOSSY, ABLE TO BE WRITTEN ON BOTH SIDES

Updates
I HAVE ATTACHED THE FILES, THEY CONSIST OF OUR CURRENT LOGO IN A FEW FORMS AND OUR BUSINESS CARD FOR THE DENTAL BRANCH, PLEASE COPY THE CURRENT DESIGN BUT ADDING THE REQUESTED CHANGES

Industry/Entity Type
Business
Contact Information for Business Card
OLMEN COSMETICS
GWEN : 0438 517 203
MARISOL : 0419 862 374
SUITE 8 HOLLOWAY COURT ARCADE
47-59 PENDRICK STREET
TALLOWMERE NSW 2389
Logo Text
OLMEN COSMETICS
Look and feel

```html
<!DOCTYPE html>
<html lang="en">
<head>
<meta charset="utf-8">
<title>Olmen Cosmetics – Business Card</title>
<link rel="stylesheet" href="https://fonts.googleapis.com/css2?family=Roboto+Condensed:wght@400;700&display=swap">
<style>
  :root {
    --page-bg: #ffffff;
    --card-bg: #ffffff;
    --card-edge: #6d6e71;
    --ink: #231f20;
    --rule: #231f20;
    --brand-green: #6abf4b;
  }
  html, body {
    margin: 0;
    padding: 0;
    width: 1200px;
    height: 1000px;
    overflow: hidden;
    background: var(--page-bg);
  }
  .canvas {
    position: relative;
    width: 1200px;
    height: 1000px;
  }
  .business-card {
    position: absolute;
    left: 172px;
    top: 248px;
    width: 853px;
    height: 500px;
    background: var(--card-bg);
    border: 1px solid var(--card-edge);
    font-family: "Roboto Condensed", "Arial Narrow", sans-serif;
    color: var(--ink);
  }
  .brand {
    position: absolute;
    left: 60px;
    top: 186px;
    display: flex;
    align-items: center;
    gap: 14px;
  }
  .brand-dot {
    width: 30px;
    height: 30px;
    border-radius: 50%;
    background: var(--brand-green);
    flex: none;
  }
  .brand-name {
    margin: 0;
    font-size: 30px;
    font-weight: 700;
    letter-spacing: 1px;
    color: var(--ink);
    white-space: nowrap;
  }
  .contact {
    position: absolute;
    left: 397px;
    top: 152px;
    font-size: 29px;
    line-height: 38px;
  }
  .address {
    margin: 0;
    font-style: normal;
    font-weight: 700;
  }
  .phones {
    margin: 39px 0 0;
    padding: 0;
    list-style: none;
    font-weight: 400;
  }
  .phone-name {
    font-weight: 700;
  }
  .appointments {
    margin: 16px 0 0;
    padding: 0;
    list-style: none;
    font-size: 24px;
    line-height: 38px;
  }
  .appointment-row {
    display: flex;
    align-items: baseline;
    gap: 8px;
    width: 410px;
  }
  .field-label {
    font-weight: 700;
    white-space: nowrap;
  }
  .write-line {
    display: inline-block;
    height: 1px;
    border-bottom: 1.5px solid var(--rule);
  }
  .write-line.date { width: 170px; margin-right: 14px; }
  .write-line.time { flex: 1; }
</style>
</head>
<body>
<main class="canvas">
  <section class="business-card" aria-label="Olmen Cosmetics business card">
    <div class="brand">
      <span class="brand-dot" aria-hidden="true"></span>
      <h1 class="brand-name">OLMEN COSMETICS</h1>
    </div>
    <div class="contact">
      <address class="address">
        Suite 8, Holloway Court Arcade<br>
        47-59 Pendrick Street,<br>
        Tallowmere, NSW 2389
      </address>
      <ul class="phones">
        <li><span class="phone-name">Gwen:</span> 0438 517 203</li>
        <li><span class="phone-name">Marisol:</span> 0419 862 374</li>
      </ul>
      <ul class="appointments">
        <li class="appointment-row">
          <span class="field-label">Date:</span><span class="write-line date"></span>
          <span class="field-label">Time:</span><span class="write-line time"></span>
        </li>
        <li class="appointment-row">
          <span class="field-label">Date:</span><span class="write-line date"></span>
          <span class="field-label">Time:</span><span class="write-line time"></span>
        </li>
      </ul>
    </div>
  </section>
</main>
</body>
</html>
```